Business Card cabinets and cabinets components making company.

the card should be formal and interesting at the same time. The main colors will be black and white.

Font styles to use
Sans Serif

Colors

Designer to choose only greyscale colors for use in the design.

Requirements
Must have
• At least must have the followings:
office phone
cell phone
address
position
name
email
web

```html
<!DOCTYPE html>
<html lang="en">
<head>
<meta charset="utf-8">
<title>Grainline – Business Card</title>
<link href="https://fonts.googleapis.com/css2?family=Poppins:wght@300;400;600&display=swap" rel="stylesheet">
<style>
  :root {
    --canvas: #e9e9e9;
    --paper: #ffffff;
    --ink: #222222;
    --ink-soft: #555555;
    --rule: #6a6a6a;
    --back: #2e2e2e;
    --back-tone: #3a3a3a;
  }
  * { box-sizing: border-box; margin: 0; padding: 0; }
  html, body {
    width: 1200px; height: 857px; overflow: hidden;
    background: var(--canvas);
    font-family: "Poppins", sans-serif;
  }
  .sheet {
    width: 1200px; height: 857px;
    display: flex; flex-direction: column;
    align-items: center; justify-content: center; gap: 40px;
  }
  .card {
    width: 600px; height: 343px;
    box-shadow: 0 6px 18px rgba(0,0,0,.18);
    position: relative;
  }
  .card-front { background: var(--paper); }
  .brand {
    position: absolute; left: 58px; top: 140px;
    display: flex; align-items: center; gap: 10px;
  }
  .brand-square { width: 22px; height: 22px; background: var(--ink); }
  .brand-name {
    font-weight: 600; font-size: 40px; color: var(--ink); line-height: 1;
  }
  .brand-rule {
    position: absolute; left: 58px; top: 200px;
    width: 212px; height: 2px; background: var(--ink);
  }
  .divider {
    position: absolute; left: 310px; top: 84px;
    width: 1px; height: 176px; background: var(--rule);
  }
  .details {
    position: absolute; left: 336px; top: 70px; color: var(--ink);
  }
  .person-name {
    font-weight: 400; font-size: 17px; letter-spacing: .5px; line-height: 1.3;
  }
  .position {
    font-weight: 300; font-size: 11px; letter-spacing: 1.5px; text-transform: uppercase;
    color: var(--ink-soft); margin-bottom: 8px;
  }
  .address {
    font-weight: 300; font-size: 12px; line-height: 1.45; color: var(--ink-soft);
    margin-bottom: 12px;
  }
  .contact-list { list-style: none; }
  .contact-item {
    display: flex; align-items: center; gap: 8px;
    font-weight: 400; font-size: 12px; line-height: 1.7; color: var(--ink);
  }
  .contact-icon { width: 10px; height: 10px; flex: none; }
  .card-back { background: var(--back); overflow: hidden; }
  .back-pattern {
    position: absolute; inset: 0;
    background: linear-gradient(135deg, var(--back) 0%, var(--back-tone) 100%);
  }
</style>
</head>
<body>
<main class="sheet">
  <section class="card card-front" aria-label="Card front">
    <div class="brand">
      <span class="brand-square"></span>
      <span class="brand-name">Grainline</span>
    </div>
    <div class="brand-rule"></div>
    <div class="divider"></div>
    <div class="details">
      <p class="person-name">DANIEL HART</p>
      <p class="position">Cabinet Designer</p>
      <p class="address">2750 Cedar Ridge Road<br>Suite 410, Austin<br>TX 78701</p>
      <ul class="contact-list">
        <li class="contact-item">
          <svg class="contact-icon" viewBox="0 0 10 10"><path d="M2 0.5 L3.8 2.6 L2.8 3.8 Q4 6 6.2 7.2 L7.4 6.2 L9.5 8 L8.3 9.5 Q3.5 9 0.5 1.7 Z" fill="currentColor"/></svg>
          +1-512-555-0148
        </li>
        <li class="contact-item">
          <svg class="contact-icon" viewBox="0 0 10 10"><rect x="2" y="0.5" width="6" height="9" rx="1" fill="none" stroke="currentColor" stroke-width="1"/></svg>
          +1-512-555-0193
        </li>
        <li class="contact-item">
          <svg class="contact-icon" viewBox="0 0 10 10"><rect x="0.5" y="2" width="9" height="6.5" fill="currentColor"/><path d="M0.5 2 L5 5.5 L9.5 2" fill="none" stroke="#fff" stroke-width="0.8"/></svg>
          info@grainlinecabinets.com
        </li>
        <li class="contact-item">
          <svg class="contact-icon" viewBox="0 0 10 10"><circle cx="5" cy="5" r="4.5" fill="currentColor"/><path d="M0.5 5 H9.5 M5 0.5 Q2 5 5 9.5 M5 0.5 Q8 5 5 9.5" fill="none" stroke="#fff" stroke-width="0.6"/></svg>
          www.grainlinecabinets.com
        </li>
      </ul>
    </div>
  </section>

  <section class="card card-back" aria-label="Card back">
    <div class="back-pattern" role="img" aria-label="Repeating tonal brand pattern on dark grey"></div>
  </section>
</main>
</body>
</html>
```